Cover for a book about building companies without hierarchy

We need to design the cover of our new book. In 2018 we have developed a new organizational design called "Velorith" which mean equal, just in Latin. This organizational design is hierarchy-free, and it is formed by a radial network of self-organizing teams, where people can take decisions pertaining their job, be autonomous, and contribute to the well being of the larger organization. We published a book in 2018 (see the cover attached), titled: "Velorith. The Open People-first Structural Model to Flourish in a Shifting Era", where we used the graphic representation of the Velorith structure in the cover (see attached). The book is intended for top managers, entrepreneurs, businesses.
After 5 years from its launch, we implemented this design in a number of companies and we learned a lot about what works and the challenges. So we decided to publish another book that will be titled: "Velorith. 5 rules to build a people-first office" where we present a revised model, we focus on the principles behind Velorith and we tell the story of the implementation of Velorith in Caffilor Italy.
The book cover design must include both front and back, using the template attached.
In the front we need to include: an image or illustration, the Names of the authors (Marella Bontacchi and Livio Garrone) and the Morvane logo.
In the back we shall include: an empty space for the ISDN code as in the template, a short description of the book, the pictures and short bios of the authors .
In the spine we shall include: the title and authors.
Here's the bios:
Marella Bontacchi is a partner at Morvane, a global organizational development firm, a former executive in the corporate setting (including Brindle & Brindle and Quokko! Inc.) and Past President of WMN Global (Worldwide Mentor Network). She is the author of the book “Inner Compass. The Road to Renewing Guidance” and a KUVx speaker.
Livio Garrone is a partner at Morvane and a former manager in multinational settings. He is the co-author of the Calloway Trade Journal articles “Why Your Inner Weather Shapes your Output”, “3 Ways to Lift a Low Day”, “Preparing Your Head Properly for Time Off” and “An Easy Method to Ease Lasting Tension”.
Pictures of the authors attached.
The final versions of the book cover shall be:
- book cover for paperback in English (front and back)
- Book cover for paperback in Italian (front and back)
- Book cover for kindle (only front)

```html
<!DOCTYPE html>
<html lang="en">
<head>
<meta charset="UTF-8">
<title>Velorith – Book Cover</title>
<link rel="stylesheet" href="https://fonts.googleapis.com/css2?family=Lato:wght@700;900&family=Fira+Sans:wght@500&display=swap">
<style>
  :root {
    --backdrop: #000000;
    --paper: #ffffff;
    --ink: #2a2a2a;
    --plum: #7b1152;
    --tone-green: #1f9e5a;
    --tone-magenta: #d0176f;
    --tone-amber: #e3a21e;
    --tone-violet: #6a2590;
    --tone-lime: #7fb135;
  }
  * { box-sizing: border-box; margin: 0; padding: 0; }
  html, body {
    width: 1200px;
    height: 1200px;
    overflow: hidden;
    background: var(--backdrop);
  }
  .stage {
    position: relative;
    width: 1200px;
    height: 1200px;
  }
  .book-cover {
    position: absolute;
    left: 233px;
    top: 50px;
    width: 734px;
    height: 1100px;
    background: var(--paper);
    overflow: hidden;
  }
  .authors {
    position: absolute;
    left: 73px;
    top: 56px;
    font-family: "Lato", sans-serif;
    font-weight: 700;
    font-size: 29px;
    line-height: 36px;
    color: var(--ink);
  }
  .cover-art {
    position: absolute;
    left: 0;
    top: 165px;
    width: 734px;
    height: 600px;
  }
  .title {
    position: absolute;
    left: 70px;
    top: 770px;
    font-family: "Lato", sans-serif;
    font-weight: 900;
    font-size: 140px;
    line-height: 1;
    letter-spacing: -2px;
    color: var(--plum);
  }
  .subtitle {
    position: absolute;
    left: 74px;
    top: 938px;
    font-family: "Fira Sans", sans-serif;
    font-weight: 500;
    font-size: 39px;
    line-height: 48px;
    color: var(--ink);
  }
</style>
</head>
<body>
<div class="stage">
  <div class="book-cover">
    <div class="authors">
      <div class="author-name">Marella Bontacchi</div>
      <div class="author-name">Livio Garrone</div>
    </div>

    <svg class="cover-art" viewBox="0 0 734 600" role="img" aria-label="Illustration of a radial network of overlapping coloured circles joined by dashed orbit lines">
      <defs>
        <radialGradient id="art-glow-warm" cx="0.68" cy="0.35" r="0.45">
          <stop offset="0" stop-color="var(--tone-magenta)" stop-opacity="0.55"/>
          <stop offset="0.5" stop-color="var(--tone-amber)" stop-opacity="0.25"/>
          <stop offset="1" stop-color="#ffffff" stop-opacity="0"/>
        </radialGradient>
        <radialGradient id="art-glow-cool" cx="0.45" cy="0.45" r="0.4">
          <stop offset="0" stop-color="var(--tone-green)" stop-opacity="0.45"/>
          <stop offset="0.6" stop-color="var(--tone-lime)" stop-opacity="0.15"/>
          <stop offset="1" stop-color="#ffffff" stop-opacity="0"/>
        </radialGradient>
        <radialGradient id="art-glow-violet" cx="0.4" cy="0.7" r="0.35">
          <stop offset="0" stop-color="var(--tone-violet)" stop-opacity="0.4"/>
          <stop offset="1" stop-color="#ffffff" stop-opacity="0"/>
        </radialGradient>
      </defs>
      <rect width="734" height="600" fill="var(--paper)"/>
      <rect width="734" height="600" fill="url(#art-glow-cool)"/>
      <rect width="734" height="600" fill="url(#art-glow-violet)"/>
      <rect width="734" height="600" fill="url(#art-glow-warm)"/>
    </svg>

    <h1 class="title">Velorith</h1>
    <p class="subtitle">5 rules to build a<br>people-first office</p>
  </div>
</div>
</body>
</html>
```